LED Bulb Packaging

We require a retail box design so some led lighting. The concept must be uniform accross a nuimber of sizes with technical information and Actual bulb image replaceable.

```html
<!DOCTYPE html>
<html lang="en">
<head>
<meta charset="utf-8">
<title>LED Corn Light – Retail Box Dieline</title>
<link rel="stylesheet" href="https://fonts.googleapis.com/css2?family=Oswald:wght@300;500;700&family=Roboto:wght@400;700&display=swap">
<style>
  :root{
    --box-blue:#0f4c9a;
    --board-grey:#e6e7e8;
    --band-yellow:#e3a623;
    --tag-black:#141414;
    --tag-green:#6cb33f;
    --tag-grey:#a7a9ac;
    --tag-sky:#7dc4ea;
    --note-yellow:#f7d417;
    --cut-orange:#f26b3a;
    --white:#ffffff;
  }
  html,body{margin:0;padding:0;width:1200px;height:499px;overflow:hidden;background:var(--white);}
  .dieline{display:block;width:1200px;height:499px;}
  .board{fill:var(--board-grey);}
  .blue{fill:var(--box-blue);}
  .white{fill:var(--white);}
  .yellow-band{fill:var(--band-yellow);}
  .title-led{font-family:'Oswald',sans-serif;font-weight:500;fill:var(--white);font-size:74px;letter-spacing:1px;}
  .title-sub{font-family:'Oswald',sans-serif;font-weight:300;fill:var(--white);font-size:15px;letter-spacing:1px;}
  .lid-led{font-family:'Oswald',sans-serif;font-weight:700;fill:var(--box-blue);font-size:50px;}
  .lid-sub{font-family:'Oswald',sans-serif;font-weight:300;fill:var(--box-blue);font-size:11px;letter-spacing:1px;}
  .tag-main{font-family:'Oswald',sans-serif;font-weight:500;fill:var(--white);font-size:9px;}
  .tag-small{font-family:'Roboto',sans-serif;fill:var(--white);font-size:3.6px;}
  .note-text{font-family:'Roboto',sans-serif;font-weight:700;fill:var(--note-yellow);font-size:5.6px;}
  .note-head{font-family:'Roboto',sans-serif;font-weight:700;fill:var(--white);font-size:6.5px;}
  .feature-label{font-family:'Roboto',sans-serif;fill:#333;font-size:4.2px;}
  .spec-line{font-family:'Roboto',sans-serif;fill:var(--white);font-size:6px;}
  .watt{font-family:'Oswald',sans-serif;font-weight:700;fill:var(--box-blue);font-size:19px;}
  .photo-slot{fill:url(#bulbTone);}
</style>
</head>
<body>
<svg class="dieline" viewBox="0 0 1386 577" preserveAspectRatio="none" xmlns="http://www.w3.org/2000/svg">
  <defs>
    <linearGradient id="bulbTone" x1="0" y1="0" x2="1" y2="0">
      <stop offset="0" stop-color="#7d8185"/>
      <stop offset="0.5" stop-color="#d9dde0"/>
      <stop offset="1" stop-color="#6f7378"/>
    </linearGradient>
    <radialGradient id="endGlow" cx="0.5" cy="0.4" r="0.6">
      <stop offset="0" stop-color="#3f7ed0"/>
      <stop offset="1" stop-color="#0f4c9a"/>
    </radialGradient>

    <g id="frontFace">
      <rect class="blue" x="0" y="0" width="454" height="170"/>
      <polygon class="white" points="257,0 454,0 454,170 330,170"/>
      <rect class="yellow-band" x="0" y="136" width="330" height="23"/>
      <!-- spec tags -->
      <g class="spec-tags">
        <polygon fill="var(--tag-black)" points="0,24 68,24 74,32 68,40 0,40"/>
        <text class="tag-main" x="22" y="33">120ML/W</text>
        <text class="tag-small" x="14" y="38.5">Luminous Efficiency</text>
        <polygon fill="var(--tag-green)" points="0,48 68,48 74,56 68,64 0,64"/>
        <text class="tag-main" x="20" y="57">50000 HRS</text>
        <text class="tag-small" x="28" y="62.5">Lifespan</text>
        <polygon fill="var(--tag-grey)" points="0,72 68,72 74,80 68,88 0,88"/>
        <text class="tag-main" x="28" y="81">95%</text>
        <text class="tag-small" x="14" y="86.5">Up To Energy Saving</text>
        <polygon fill="var(--tag-sky)" points="0,94 68,94 74,102 68,110 0,110"/>
        <text class="tag-main" x="27" y="105">IP64</text>
      </g>
      <text class="title-led" x="120" y="87">LED</text>
      <text class="title-sub" x="124" y="108">CORN LIGHT</text>
      <!-- certification badges -->
      <g class="cert-badges" fill="none" stroke="var(--white)" stroke-width="1.3">
        <circle cx="115" cy="148" r="6"/>
        <rect x="131" y="142" width="12" height="12"/>
        <circle cx="160" cy="148" r="6"/>
        <circle cx="180" cy="148" r="6"/>
        <circle cx="204" cy="148" r="6"/>
        <rect x="220" y="142" width="14" height="12"/>
      </g>
      <rect class="photo-slot" x="290" y="14" width="84" height="140" rx="14" role="img" aria-label="Product photo of the LED corn light bulb"/>
    </g>
  </defs>

  <!-- glue flap -->
  <path class="board" d="M52 266 L98 248 V418 L52 402 Z"/>

  <!-- side panel A -->
  <path class="board" d="M98 248 L190 158 H460 L552 248 Z"/>
  <path class="board" d="M98 418 L210 500 V540 Q210 550 220 550 H540 Q550 550 550 540 V430 L552 418 Z"/>
  <use href="#frontFace" x="98" y="248"/>
  <g class="hang-cutout">
    <line x1="232" y1="246" x2="416" y2="246" stroke="var(--cut-orange)" stroke-width="0.8"/>
    <rect x="288" y="210" width="72" height="72" rx="8" fill="var(--white)" stroke="var(--cut-orange)" stroke-width="0.8"/>
  </g>

  <!-- side panel B (notes) -->
  <path class="board" d="M552 248 L640 158 H723 V248 Z"/>
  <path class="board" d="M552 418 H723 V455 L700 470 V550 H552 Z"/>
  <rect class="blue" x="552" y="248" width="171" height="170"/>
  <g class="notes">
    <text class="note-head" x="566" y="265">NOTE:</text>
    <text class="note-text" x="566" y="275">• Before install or replace the lamps please cut off</text>
    <text class="note-text" x="570" y="282">the switch.</text>
    <text class="note-text" x="566" y="290">• After installed,when lamp work normal,pls note</text>
    <text class="note-text" x="570" y="297">not take off the driver with electriferous.</text>
    <text class="note-text" x="566" y="305">• After lighting a long time,the lamps can be reach</text>
    <text class="note-text" x="570" y="312">60°C,Pls be careful to take off the lamps avoid scald.</text>
    <text class="note-text" x="566" y="320">• Interior driver is constant current.</text>
    <text class="note-text" x="566" y="327">• Work temperature is -20~40°C.</text>
  </g>
  <g class="energy-label">
    <rect x="565" y="338" width="56" height="70" fill="var(--white)" stroke="#222" stroke-width="0.8"/>
    <rect x="606" y="341" width="12" height="8" fill="var(--box-blue)"/>
    <rect x="606" y="352" width="12" height="10" fill="#222"/>
    <rect x="568" y="356" width="10" height="5" fill="#00a651"/>
    <rect x="568" y="363" width="13" height="5" fill="#50b848"/>
    <rect x="568" y="370" width="16" height="5" fill="#bfd730"/>
    <rect x="568" y="377" width="19" height="5" fill="#fff200"/>
    <rect x="568" y="384" width="22" height="5" fill="#fdb913"/>
    <rect x="568" y="391" width="25" height="5" fill="#f37021"/>
    <rect x="568" y="398" width="28" height="5" fill="#ed1c24"/>
  </g>

  <!-- lid with hang tab -->
  <path class="blue" d="M860 74 V45 Q860 32 873 32 H1027 Q1040 32 1040 45 V74 Z"/>
  <rect class="white" x="905" y="66" width="90" height="12"/>
  <circle class="white" cx="950" cy="76" r="10"/>
  <path class="board" d="M723 78 H1177 V248 H723 Z"/>
  <rect class="blue" x="723" y="100" width="454" height="60"/>
  <rect class="white" x="723" y="127" width="454" height="4"/>
  <g class="features">
    <g transform="translate(785 110)"><rect class="white" width="34" height="45"/><circle cx="17" cy="33" r="6" fill="#6cb33f"/><text class="feature-label" transform="rotate(180 17 14)" x="6" y="12">No</text><text class="feature-label" transform="rotate(180 17 14)" x="5" y="18">Radiation</text></g>
    <g transform="translate(828 110)"><rect class="white" width="34" height="45"/><circle cx="17" cy="33" r="6" fill="var(--white)" stroke="#ccc" stroke-width="0.6"/><text class="feature-label" transform="rotate(180 17 14)" x="5" y="15">No Flicker</text></g>
    <g transform="translate(870 110)"><rect class="white" width="34" height="45"/><circle cx="17" cy="33" r="6" fill="#6cb33f"/><text class="feature-label" transform="rotate(180 17 14)" x="4" y="12">Low-carbon</text><text class="feature-label" transform="rotate(180 17 14)" x="9" y="18">Green</text></g>
    <g transform="translate(912 110)"><rect class="white" width="34" height="45"/><circle cx="17" cy="33" r="6" fill="#6cb33f"/><text class="feature-label" transform="rotate(180 17 14)" x="8" y="12">Protect</text><text class="feature-label" transform="rotate(180 17 14)" x="5" y="18">Your Eyes</text></g>
    <g transform="translate(954 110)"><rect class="white" width="34" height="45"/><circle cx="17" cy="33" r="6" fill="#6cb33f"/><text class="feature-label" transform="rotate(180 17 14)" x="8" y="12">Energy</text><text class="feature-label" transform="rotate(180 17 14)" x="8" y="18">Saving</text></g>
    <g transform="translate(996 110)"><rect class="white" width="34" height="45"/><circle cx="17" cy="33" r="6" fill="#6cb33f"/><text class="feature-label" transform="rotate(180 17 14)" x="8" y="15">Quality</text></g>
    <g transform="translate(1038 110)"><rect class="white" width="34" height="45"/><circle cx="17" cy="33" r="6" fill="#6cb33f"/><text class="feature-label" transform="rotate(180 17 14)" x="7" y="15">Long-life</text></g>
    <g transform="translate(1080 110)"><rect class="white" width="34" height="45"/><circle cx="17" cy="33" r="6" fill="#6cb33f"/><text class="feature-label" transform="rotate(180 17 14)" x="10" y="12">High</text><text class="feature-label" transform="rotate(180 17 14)" x="4" y="18">Brightness</text></g>
  </g>
  <g transform="rotate(180 950 200)">
    <text class="lid-led" x="918" y="212">LED</text>
    <text class="lid-sub" x="920" y="226">CORN LIGHT</text>
  </g>

  <!-- front panel -->
  <path class="board" d="M723 418 H1177 V460 L1090 540 H820 L760 470 H723 Z"/>
  <use href="#frontFace" x="723" y="248"/>

  <!-- end panel -->
  <path class="board" d="M1177 248 V158 H1260 L1340 248 Z"/>
  <path class="board" d="M1177 418 H1340 L1270 495 V540 Q1270 550 1260 550 H1187 Q1177 550 1177 540 Z"/>
  <rect x="1177" y="248" width="163" height="170" fill="url(#endGlow)"/>
  <g class="wattage-icon">
    <path class="white" d="M1258 284 a34 34 0 0 1 20 61 v10 h-40 v-10 a34 34 0 0 1 20 -61 Z"/>
    <rect class="white" x="1241" y="359" width="34" height="4" rx="2"/>
    <rect class="white" x="1243" y="366" width="30" height="4" rx="2"/>
    <rect class="white" x="1248" y="373" width="20" height="4" rx="2"/>
    <path d="M1240 300 a24 24 0 0 1 24 -10" fill="none" stroke="var(--box-blue)" stroke-width="6"/>
    <text class="watt" x="1244" y="331">27W</text>
  </g>
  <text class="spec-line" x="1223" y="399">50000 hrs    .IP64    .120lm</text>
</svg>
</body>
</html>
```